TRUCK WASH OUTDOOR DRIVE THROUGH MENU CONTEST

WE NEED A DRIVE THROUGH MENU WITH OUR SERVICES AND PRICES. I HAVE ATTACHED A FEW EXAMPLES THAT I STARTED.

I WANT THIS TO BE EYE CATCHING WITH BRIGHT COLORS

Target Market(s)

TRUCK WASH AND DETAIL SHOP, TRANSPORTATION.

Requirements
Must have
• INCORPORATE MY LOGO INTO THE SIGN.
• FINAL PROJECT MUST BE IN .AI FORMAT.
• COMPANY COLORS ARE RED AND BLUE

```html
<!DOCTYPE html>
<html lang="en">
<head>
<meta charset="utf-8">
<title>The Rig Rinse – Wash Prices</title>
<link rel="stylesheet" href="https://fonts.googleapis.com/css2?family=Fredoka:wght@500;600;700&family=Varela+Round&display=swap">
<style>
  :root{
    --black:#000;
    --white:#fff;
    --red:#e8212e;
    --sky:#2fa9e2;
    --navy:#0f3b7a;
    --panel-top:#dff0fb;
    --panel-bottom:#a9cbe8;
    --water-light:#cfe9f8;
    --water-deep:#1f6fb8;
    --platinum:#f1f3f4;
    --platinum-dark:#b9bdc2;
    --gold:#e4ab28;
    --gold-dark:#a87812;
    --silver:#c9c9c9;
    --silver-dark:#8f9194;
    --express:#4fb9e8;
    --express-dark:#2b86b8;
  }
  *{box-sizing:border-box;margin:0;padding:0}
  html,body{width:848px;height:1200px;overflow:hidden;background:var(--black)}
  .sign{position:relative;width:848px;height:1200px;background:var(--black);font-family:"Varela Round",sans-serif}

  .header{position:absolute;left:0;top:20px;width:848px;height:240px;background:var(--white)}
  .logo-box{position:absolute;left:41px;top:22px;width:222px;height:198px;border:1px solid #333;display:flex;align-items:center;justify-content:center;gap:10px}
  .logo-box .dot{width:22px;height:22px;border-radius:50%;background:var(--red)}
  .logo-box .brand{font-family:"Fredoka",sans-serif;font-weight:700;font-size:30px;color:var(--red);line-height:1}
  .headline{position:absolute;left:285px;top:0;width:540px;height:240px;display:flex;align-items:center;justify-content:center;font-family:"Fredoka",sans-serif;font-weight:700;font-size:74px;color:var(--red)}

  .water-band{position:absolute;left:0;top:260px;width:848px;height:155px;background:radial-gradient(ellipse at 30% 40%,var(--water-light),#7cc0ea 45%,var(--water-deep))}
  .size-pill{position:absolute;left:48px;top:300px;width:752px;height:80px;border-radius:40px;background:var(--water-deep);border:5px solid var(--white);display:flex;align-items:center;justify-content:center}
  .size-pill h1{font-family:"Fredoka",sans-serif;font-weight:700;font-size:47px;color:var(--red);-webkit-text-stroke:2px var(--white);paint-order:stroke fill;letter-spacing:.2px}

  .section-title{position:absolute;left:43px;top:424px;font-family:"Fredoka",sans-serif;font-weight:600;font-size:40px;color:var(--white)}

  .price-panel{position:absolute;left:42px;top:478px;width:764px;height:680px;background:linear-gradient(180deg,var(--panel-top),var(--panel-bottom))}

  .tier{position:absolute;left:0;width:848px;height:130px}
  .tier svg{position:absolute;left:0;top:0}
  .tag{position:absolute;top:0;height:88px;border-radius:0 30px 30px 0;box-shadow:0 3px 6px rgba(0,0,0,.25);display:flex;flex-direction:column;align-items:center;justify-content:center}
  .tag-name{left:17px;width:200px;border-radius:0 30px 30px 0}
  .tag-price{left:635px;width:198px;border-radius:30px 0 0 30px}
  .tag-name strong{font-family:"Fredoka",sans-serif;font-weight:700;font-size:34px;color:var(--navy);line-height:1}
  .tag-name small{font-family:"Fredoka",sans-serif;font-weight:600;font-size:14px;color:var(--navy);margin-top:2px}
  .tag-price span{font-family:"Fredoka",sans-serif;font-weight:700;font-size:54px;color:var(--navy)}
  .services{position:absolute;left:222px;top:18px;width:410px;text-align:center;font-size:22.5px;line-height:25px;color:#1b1b1b}

  .tier-platinum{top:521px}
  .tier-gold{top:672px}
  .tier-silver{top:823px}
  .tier-express{top:975px}
  .tier-platinum .tag{background:var(--platinum)}
  .tier-gold .tag{background:var(--gold)}
  .tier-silver .tag{background:var(--silver)}
  .tier-express .tag{background:var(--express)}
  .tier-express .services{top:31px}

  .footer-note{position:absolute;left:42px;top:1098px;width:764px;text-align:center;font-family:"Fredoka",sans-serif;font-weight:600;font-size:27px;color:var(--navy)}
</style>
</head>
<body>
<main class="sign">
  <header class="header">
    <div class="logo-box"><span class="dot"></span><span class="brand">The Rig Rinse</span></div>
    <div class="headline">The Rig Rinse</div>
  </header>

  <div class="water-band" role="img" aria-label="Background of blue water bubbles and splashes"></div>
  <div class="size-pill"><h1>Standard Tractor &amp; Trailer (53’)</h1></div>

  <h2 class="section-title">Wash Prices</h2>

  <section class="price-panel" role="img" aria-label="Light blue grid paper backdrop with water droplets"></section>

  <div class="tier tier-platinum">
    <svg width="848" height="130"><path d="M17 40 V120 Q17 130 30 128 L200 118 V60 Z" fill="var(--platinum-dark)"/><path d="M833 40 V120 Q833 130 820 128 L650 118 V60 Z" fill="var(--platinum-dark)"/></svg>
    <div class="tag tag-name"><strong>PLATINUM</strong><small>Undercarriage rinse</small></div>
    <p class="services">PreSoak • Soap and Scrub • Rinse<br>• Tire Shine • Platinum Protection</p>
    <div class="tag tag-price"><span>$130</span></div>
  </div>

  <div class="tier tier-gold">
    <svg width="848" height="130"><path d="M17 40 V120 Q17 130 30 128 L200 118 V60 Z" fill="var(--gold-dark)"/><path d="M833 40 V120 Q833 130 820 128 L650 118 V60 Z" fill="var(--gold-dark)"/></svg>
    <div class="tag tag-name"><strong>GOLD</strong><small>Undercarriage rinse</small></div>
    <p class="services">PreSoak • Soap and Scrub • Rinse<br>• Tire Shine • Gloss Coat Polish</p>
    <div class="tag tag-price"><span>$120</span></div>
  </div>

  <div class="tier tier-silver">
    <svg width="848" height="130"><path d="M17 40 V120 Q17 130 30 128 L200 118 V60 Z" fill="var(--silver-dark)"/><path d="M833 40 V120 Q833 130 820 128 L650 118 V60 Z" fill="var(--silver-dark)"/></svg>
    <div class="tag tag-name"><strong>SILVER</strong><small>Undercarriage rinse</small></div>
    <p class="services">PreSoak • Soap and Scrub • Rinse<br>• Tire Shine</p>
    <div class="tag tag-price"><span>$85</span></div>
  </div>

  <div class="tier tier-express">
    <svg width="848" height="130"><path d="M17 40 V120 Q17 130 30 128 L200 118 V60 Z" fill="var(--express-dark)"/><path d="M833 40 V120 Q833 130 820 128 L650 118 V60 Z" fill="var(--express-dark)"/></svg>
    <div class="tag tag-name"><strong>EXPRESS</strong><small>Undercarriage rinse</small></div>
    <p class="services">PreSoak • Soap and Scrub • Rinse</p>
    <div class="tag tag-price"><span>$75</span></div>
  </div>

  <p class="footer-note">FOR MORE OPTIONS PLEASE ASK FRONT DESK</p>
</main>
</body>
</html>
```